Zorpax.com (Dedicated servers Provider)

We provide dedicated servers for clients around the world. We have created a layout for you. You need to create exactly the design based on these sketches. All text, you can take from our sketches (later we will replace them).

Target Market(s)

Web site owners and web developers

Requirements
Should not have
• The design should not use old-style fonts.

```html
<!DOCTYPE html>
<html lang="en">
<head>
<meta charset="utf-8">
<title>Zorpax – Dedicated Servers</title>
<link href="https://fonts.googleapis.com/css2?family=Arimo:wght@400;700&family=Yanone+Kaffeesatz:wght@400;500&display=swap" rel="stylesheet">
<style>
:root{
  --header-dark:#2c3139;
  --header-mid:#4a505a;
  --lime:#a9c23a;
  --lime-dark:#7e9517;
  --olive-dark:#5e5c0c;
  --blue-dark:#17609a;
  --sky:#5cc3ec;
  --text:#333;
  --panel:#f1f1f1;
  --line:#d6d6d6;
  --red:#b3262b;
  --footer-text:#d8d8d8;
}
*{box-sizing:border-box;margin:0;padding:0}
html,body{width:874px;height:1200px;overflow:hidden}
body{position:relative;background:#fff;font-family:Arimo,Arial,sans-serif;color:var(--text)}
.abs{position:absolute}
.header{left:0;top:0;width:874px;height:405px;background:radial-gradient(ellipse at 45% 40%,var(--header-mid),var(--header-dark) 75%)}
.brand{left:60px;top:20px;display:flex;align-items:center;gap:8px;color:#fff;font-weight:700;font-size:30px;letter-spacing:.5px}
.brand-mark{width:22px;height:22px;background:var(--lime)}
.phone{right:64px;top:8px;color:#fff;font-weight:700;font-size:14px;display:flex;align-items:center;gap:6px}
.toplinks{right:64px;top:37px;color:#fff;font-size:9px}
.nav-link{top:59px;font-size:11px;font-weight:700;color:#fff;line-height:14px}
.nav-home{left:224px;top:53px;width:52px;height:25px;line-height:25px;text-align:center;background:linear-gradient(#c8d94c,var(--lime-dark));border-radius:4px}
.nav-order{top:57px;color:var(--lime);font-size:14px;font-weight:700;line-height:16px}
.hero-title{left:60px;top:110px;color:#fff;font-family:"Yanone Kaffeesatz",sans-serif;font-weight:400;font-size:52px;letter-spacing:.5px;line-height:1}
.hero-list{left:60px;top:178px;list-style:none;color:#fff;font-size:14px}
.hero-list li{height:29.2px;padding-left:16px;position:relative}
.hero-list li::before{content:"";position:absolute;left:1px;top:4px;border-left:5px solid var(--lime);border-top:4px solid transparent;border-bottom:4px solid transparent}
.btn-more{left:61px;top:332px;width:130px;height:32px;border-radius:4px;background:linear-gradient(#5db6ea,var(--blue-dark));color:#fff;font-weight:700;font-size:15px;text-align:center;line-height:30px;border:1px solid #8dd0f5}
.hero-art{left:448px;top:85px;width:426px;height:345px;background:linear-gradient(180deg,rgba(62,150,120,.35) 0%,rgba(40,44,50,.55) 40%,rgba(30,32,36,.6) 75%,rgba(255,255,255,0) 100%)}
.testi-tab{left:60px;top:419px;width:118px;height:22px;background:#3b4049;color:#fff;font-family:"Yanone Kaffeesatz",sans-serif;font-size:14px;line-height:22px;padding-left:42px}
.testi-tab::before{content:"";position:absolute;left:0;top:0;width:28px;height:22px;background:#c68a34}
.testi-box{left:60px;top:441px;width:751px;height:105px;border:1px solid var(--line);background:linear-gradient(#fff,#ececec)}
.testi-photo{left:72px;top:451px;width:83px;height:84px;border:3px solid #e1a34a;background:linear-gradient(#b49468,#e6c8a6)}
.testi-name{left:75px;top:512px;width:77px;height:20px;background:rgba(40,40,40,.85);color:#fff;font-family:"Yanone Kaffeesatz",sans-serif;font-size:13px;text-align:center;line-height:20px}
.testi-quote{left:178px;top:452px;font-size:62px;font-weight:700;color:#444;line-height:1}
.testi-text{left:217px;top:473px;width:580px;font-size:17px;color:#444;line-height:22px}
.tab{top:563px;height:24px;font-size:11px;font-weight:700;text-align:center;line-height:24px;border-radius:3px 3px 0 0}
.tab-on{left:60px;width:170px;background:#f2f2f2;border:1px solid var(--line);border-bottom:none;color:#333;height:25px}
.tab-off{width:171px;background:linear-gradient(#9fe0f7,var(--sky));color:#1a5c7a}
.panel{left:60px;top:587px;width:751px;height:303px;border:1px solid var(--line);background:#fff}
.card{top:605px;height:151px;border:1px solid var(--line);background:linear-gradient(#fff,#f1f1f1)}
.card-art{position:absolute;top:10px;width:130px;height:50px;background:linear-gradient(90deg,#6aa43b 0 32%,#2f3134 32%);border-radius:4px}
.plan-lbl{position:absolute;top:70px;font-size:7px;font-weight:700;white-space:nowrap}
.price{position:absolute;top:76px;font-weight:700;font-size:36px;letter-spacing:-1px;color:#222;line-height:40px}
.price sup{font-size:15px;vertical-align:18px}
.price small{font-size:20px;vertical-align:13px}
.permo{position:absolute;top:102px;font-size:6px}
.specs{position:absolute;top:68px;font-size:8.5px;line-height:13.5px;white-space:nowrap}
.select{position:absolute;top:106px;width:100px;height:13px;border:1px solid #aaa;background:#fff;font-size:7.5px;padding-left:5px;line-height:11px}
.all-link{position:absolute;top:134px;font-size:8px;text-decoration:underline}
.btn-order{position:absolute;top:124px;width:65px;height:20px;border-radius:3px;background:linear-gradient(#b3b03a,var(--olive-dark));color:#fff;font-size:11px;font-weight:700;text-align:center;line-height:20px}
.features{left:61px;top:768px;width:749px;height:121px;background:var(--panel);border-top:1px solid var(--line)}
.map{left:75px;top:780px;width:140px;height:85px;background:radial-gradient(ellipse,#8fc4e6,#cfd5da 70%,transparent 72%)}
.feat{font-size:11.5px;font-weight:700;display:flex;align-items:center;gap:7px}
.tick{width:17px;height:17px;border-radius:50%;background:var(--red);display:flex;align-items:center;justify-content:center}
.partners{left:60px;top:910px;width:751px;height:73px;border:1px solid var(--line);background:linear-gradient(#fff,#efefef)}
.arrow{position:absolute;top:20px;width:0;height:0;border-top:16px solid transparent;border-bottom:16px solid transparent}
.badge{position:absolute;top:27px;height:20px;background:#b9b9b9;border-radius:3px}
.footer{left:0;top:1010px;width:874px;height:190px;background:linear-gradient(#3a3a3a,#151515);color:var(--footer-text)}
.fcol{position:absolute;top:18px;font-size:9px;line-height:13.5px}
.fcol h3{font-weight:400;font-size:14px;color:#fff;margin-bottom:14px}
.fcol p{margin-bottom:13px}
.fsep{position:absolute;top:15px;width:1px;height:138px;background:#555}
.qlinks{list-style:none}
.qlinks li{height:22px;padding-left:14px;position:relative}
.qlinks li::before{content:"›";position:absolute;left:0;top:-3px;font-size:13px}
.field{width:160px;background:#6b6b6b;border:1px solid #888;color:#ddd;font-size:8.5px;padding:4px 6px;margin-bottom:8px}
.btn-submit{width:52px;height:24px;border-radius:4px;background:linear-gradient(#e1ec5e,var(--lime-dark));color:#fff;font-weight:700;font-size:11px;text-align:center;line-height:24px}
.copy{left:60px;top:1176px;font-size:9px;color:#999;border-top:1px solid #444;width:751px;padding-top:8px}
</style>
</head>
<body>
<header class="abs header"></header>
<div class="abs hero-art" role="img" aria-label="Globe above a row of server towers"></div>
<div class="abs brand"><span class="brand-mark"></span>zorpax</div>
<div class="abs phone"><svg width="13" height="13" viewBox="0 0 13 13"><rect width="13" height="13" rx="2" fill="#fff"/><path d="M4 3c0 4 2 6 6 7l1-2-2-1-1 1C7 7 6 6 5 5l1-1-1-2z" fill="#2c3139"/></svg>Phone Number</div>
<div class="abs toplinks">User Registration &nbsp;|&nbsp; Customer Login &nbsp;|&nbsp; Live Chat Online</div>
<nav>
  <span class="abs nav-link nav-home">Home</span>
  <span class="abs nav-link" style="left:297px">Domains</span>
  <span class="abs nav-link" style="left:377px">Web Hosting</span>
  <span class="abs nav-link" style="left:476px">Latest News</span>
  <span class="abs nav-link" style="left:572px">My Account</span>
  <span class="abs nav-link" style="left:667px">Contact</span>
  <span class="abs nav-order" style="left:743px">Order Now</span>
</nav>
<h1 class="abs hero-title">DEDICATED SERVERS</h1>
<ul class="abs hero-list"><li>Self Owned Date Center</li><li>24 x 7 x 365 On-Site Support</li><li>100% Uptime Guarantee</li><li>Industry Leading Control Panel</li><li>Custom Servers, 24 hours setup</li></ul>
<div class="abs btn-more">Find Out More</div>

<div class="abs testi-tab">TESTIMONIAL</div>
<div class="abs testi-box"></div>
<div class="abs testi-photo" role="img" aria-label="Portrait of the customer"></div>
<div class="abs testi-name">MARIN TOLVEY</div>
<div class="abs testi-quote">“</div>
<p class="abs testi-text">Fusce molestie euismod leo at vulputate. Etiam id nibh ac nulla adipiscing euismod. Sed lobortis blandit gravida. Suspendisse potenti.</p>

<div class="abs tab tab-on">Dedicated servers</div>
<div class="abs tab tab-off" style="left:242px">Web Hosting</div>
<div class="abs tab tab-off" style="left:424px">Virtual Private Servers</div>
<div class="abs panel"></div>

<div class="abs card" style="left:80px;width:208px">
  <div class="card-art" style="left:32px" role="img" aria-label="Processor chip beside a server unit"></div>
  <span class="plan-lbl" style="left:34px">Plans starting at</span>
  <div class="price" style="left:11px"><sup>$</sup>39<small>00</small></div>
  <span class="permo" style="left:68px">per mo.</span>
  <div class="specs" style="left:99px">80GB SATA HD<br>1GB RAM<br>1TB Bandwidth</div>
  <div class="select" style="left:99px">1 year - 39.00/mo</div>
  <span class="all-link" style="left:18px">All Dedicated Servers</span>
  <div class="btn-order" style="left:115px">ORDER</div>
</div>
<div class="abs card" style="left:315px;width:219px">
  <div class="card-art" style="left:42px" role="img" aria-label="Processor chip beside a server unit"></div>
  <span class="plan-lbl" style="left:43px">Plans starting at</span>
  <div class="price" style="left:8px"><sup>$</sup>219<small>00</small></div>
  <span class="permo" style="left:78px">per mo.</span>
  <div class="specs" style="left:109px">500 SATA HD<br>6GB RAM<br>8TB Bandwidth</div>
  <div class="select" style="left:109px;width:102px">1 year - 219.00/mo</div>
  <span class="all-link" style="left:28px">All Dedicated Servers</span>
  <div class="btn-order" style="left:125px">ORDER</div>
</div>
<div class="abs card" style="left:565px;width:223px">
  <div class="card-art" style="left:42px" role="img" aria-label="Processor chip beside a server unit"></div>
  <span class="plan-lbl" style="left:43px">Plans starting at</span>
  <div class="price" style="left:9px"><sup>$</sup>395<small>00</small></div>
  <span class="permo" style="left:79px">per mo.</span>
  <div class="specs" style="left:110px">1000 SATA HD<br>16GB RAM<br>10TB Bandwidth</div>
  <div class="select" style="left:110px;width:103px">1 year - 395.00/mo</div>
  <span class="all-link" style="left:28px">All Dedicated Servers</span>
  <div class="btn-order" style="left:125px">ORDER</div>
</div>

<div class="abs features"></div>
<div class="abs map" role="img" aria-label="Map of the United States with data center links"></div>
<div class="abs feat" style="left:315px;top:790px"><span class="tick"><svg width="9" height="9" viewBox="0 0 9 9"><path d="M1 5l2 2 5-6" stroke="#fff" stroke-width="1.8" fill="none"/></svg></span>100% Network Uptime SLA</div>
<div class="abs feat" style="left:315px;top:820px"><span class="tick"><svg width="9" height="9" viewBox="0 0 9 9"><path d="M1 5l2 2 5-6" stroke="#fff" stroke-width="1.8" fill="none"/></svg></span>ISO 9001:2008 Certified</div>
<div class="abs feat" style="left:315px;top:850px"><span class="tick"><svg width="9" height="9" viewBox="0 0 9 9"><path d="M1 5l2 2 5-6" stroke="#fff" stroke-width="1.8" fill="none"/></svg></span>24/7 ITIL Technical Support</div>
<div class="abs feat" style="left:527px;top:790px"><span class="tick"><svg width="9" height="9" viewBox="0 0 9 9"><path d="M1 5l2 2 5-6" stroke="#fff" stroke-width="1.8" fill="none"/></svg></span>3 SSAE-16 Certified Data Centers</div>
<div class="abs feat" style="left:527px;top:820px"><span class="tick"><svg width="9" height="9" viewBox="0 0 9 9"><path d="M1 5l2 2 5-6" stroke="#fff" stroke-width="1.8" fill="none"/></svg></span>Coast-to-Coast IP Backbone</div>
<div class="abs feat" style="left:527px;top:850px"><span class="tick"><svg width="9" height="9" viewBox="0 0 9 9"><path d="M1 5l2 2 5-6" stroke="#fff" stroke-width="1.8" fill="none"/></svg></span>Award Winning Since 1996</div>

<div class="abs partners">
  <span class="arrow" style="left:18px;border-right:18px solid var(--sky)"></span>
  <span class="badge" style="left:75px;width:40px;border-radius:50%"></span>
  <span class="badge" style="left:148px;width:20px"></span>
  <span class="badge" style="left:188px;width:50px"></span>
  <span class="badge" style="left:268px;width:55px"></span>
  <span class="badge" style="left:347px;width:48px"></span>
  <span class="badge" style="left:425px;width:36px"></span>
  <span class="badge" style="left:493px;width:44px"></span>
  <span class="badge" style="left:563px;width:52px"></span>
  <span class="badge" style="left:640px;width:40px"></span>
  <span class="arrow" style="left:713px;border-left:18px solid var(--sky)"></span>
</div>

<footer class="abs footer">
  <div class="fcol" style="left:60px;width:185px"><h3>Keep it Simple</h3><p>Aliquam erat volutpat. Ut ut neque quam. Etiam ullamcorper dictum varius. Phasellus sit amet turpis neque. Cras ultricies, odio commodo congue viverra.</p><p>Donec orci mauris, vestibulum</p></div>
  <span class="fsep" style="left:263px"></span>
  <div class="fcol" style="left:284px;width:175px"><h3>About Us</h3><p>Aliquam erat volutpat. Ut ut neque quam. Etiam ullamcorper dictum varius. Phaslus sit amet turpis neque. Cras ultricies, odio commodo congue viverra.</p><p>Donec orci mauris, vestibulum</p></div>
  <span class="fsep" style="left:467px"></span>
  <div class="fcol" style="left:489px"><h3>Quick Links</h3><ul class="qlinks"><li>Aliquam erat volutpat.</li><li>Aliquam erat volutpat.</li><li>Aliquam erat volutpat.</li><li>Aliquam erat volutpat.</li></ul></div>
  <span class="fsep" style="left:627px"></span>
  <div class="fcol" style="left:648px"><h3>Contact Us</h3><div class="field">Name</div><div class="field" style="height:32px">Message</div><div class="btn-submit">Submit</div></div>
</footer>
<div class="abs copy">Copyrights © 2012. All Rights Reserved.</div>
</body>
</html>
```